New homepage concept needed for online reading programs website

About the Academy of Literacy Growth:
The Institute teaches online summer reading skills programs for entering fourth graders, offered through partnerships with universities, colleges, and municipalities nationwide. The goal of the program is to build reading skills (long-word decoding, fluency and comprehension), and foster a lifelong love of books and reading.

Aims & Target Market:
The Institute has developed a new format of its online reading program for fourth graders, which includes live small-group video classes taught by a professional reading teacher. The Institute seeks a mock-up of a homepage of the website used to market this new program. The primary audience for this website is the parents of these 4th graders. Traffic to this website is driven by direct-marketing campaigns directed at parents and students.

Live classes for children are completely new in online education, unlike anything else in the marketplace, and parents therefor have no experience with them. The successful homepage mock-up will include illustrations or photographs that allow visitors to immediately grasp/understand the new format, without relying on a written description. Additionally, the successful homepage concept will make the program, and the video classes in particular, feel fun and appealing to kids and parents alike.

There are three main elements to the program, and each needs to be represented graphically on the homepage, with particular emphasis on the small-group video classes:
1. Live small-group video classes (weekly for six weeks):
a. During video class discussions, the student’s computer (or tablet) screen is filled with live video frames of the teacher and the other students. The video frame for the teacher is larger, and the other students appear in smaller frames.
b. During other video class instruction, the teacher uses a presentation screen to display pages of a book or a “whiteboard” used for instructional activities.
c. The homepage mock-up could include a screenshot of the video classes themselves, with children looking engaged and a teacher leading them in discussion. We have included a screen shot of one of these classes for reference, but do not feel constrained to represent this screen realistically (as shown here). It can be changed around – teacher in the center, etc.). Alternately, if there is a graphic other than a screen shot that you feel could be used to bring across the concept of the video classes, feel free.
2. Individualized online instruction
a. Graphics could include screenshots of the video lessons students complete in between these weekly classes and/or images of a child or children at computer(s).
3. Independent reading in great books
a. Graphics could include some or all of the program books, which can be pulled from our current website (link below), and/or images of a child or children reading.

An example of our current online program website can be seen at http://fenwick.webliteracystudio.example/4/Home. Please reference this site for information on program goals, books/materials, and site navigation.
The successful design will be welcoming and inviting, and allow parents and students to immediately grasp what the programs are, with particular emphasis on the live small-group video classes.

Copy and Specifications:
Sample copy has been provided for reference, as well as a screen shot of our sample classes to show what students will see on screen. Also included are stills of our online video lessons to illustrate the online instruction aspect.

```html
<!DOCTYPE html>
<html lang="en">
<head>
<meta charset="utf-8">
<title>Academy of Literacy Growth — Live Classes</title>
<link rel="stylesheet" href="https://fonts.googleapis.com/css2?family=Source+Sans+3:wght@400;600;700&family=Kaushan+Script&display=swap">
<style>
  :root {
    --brand-red: #d71920;
    --nav-blue: #1aa3cf;
    --nav-blue-dark: #0f88b3;
    --text-body: #2b2b2b;
    --script-blue: #2168b3;
    --footer-bg: #333333;
    --footer-text: #ffffff;
    --footer-mark: #9a9a9a;
    --social-navy: #1e4f7a;
    --social-sky: #2ea7e0;
    --social-orange: #f0921c;
    --social-grey: #b5b5b5;
    --frame-border: #d6d6d6;
  }
  * { box-sizing: border-box; margin: 0; padding: 0; }
  html, body { width: 1112px; height: 1200px; overflow: hidden; background: #fff; }
  body { font-family: "Source Sans 3", Arial, sans-serif; color: var(--text-body); position: relative; }

  .site-header { position: absolute; left: 0; top: 0; width: 1112px; height: 120px; }
  .brand-name { position: absolute; left: 98px; top: 30px; font-size: 30px; line-height: 32px; font-weight: 600; color: var(--brand-red); }
  .search-box { position: absolute; left: 445px; top: 40px; width: 330px; height: 36px; border: 1px solid #cfcfcf; background: #f4f4f4; }
  .search-box span { position: absolute; left: 11px; top: 8px; font-size: 14px; color: #9a9a9a; }
  .search-box .search-divider { position: absolute; right: 36px; top: 4px; width: 1px; height: 26px; background: #cfcfcf; }
  .search-box svg { position: absolute; right: 9px; top: 8px; }
  .social-links { position: absolute; left: 809px; top: 34px; display: flex; gap: 12px; }
  .social-links .social-dot { width: 42px; height: 42px; border-radius: 50%; display: flex; align-items: center; justify-content: center; }
  .social-dot.navy { background: var(--social-navy); }
  .social-dot.sky { background: var(--social-sky); }
  .social-dot.orange { background: var(--social-orange); }
  .social-dot.grey { background: var(--social-grey); }

  .main-nav { position: absolute; left: 0; top: 120px; width: 1112px; height: 49px; background: linear-gradient(var(--nav-blue), var(--nav-blue-dark)); }
  .main-nav a { position: absolute; top: 15px; font-size: 15px; font-weight: 700; color: #fff; text-decoration: none; letter-spacing: 0.2px; }
  .main-nav .nav-sep { position: absolute; top: 9px; width: 1px; height: 31px; background: rgba(255,255,255,0.28); }

  .hero { position: absolute; left: 0; top: 169px; width: 1112px; height: 395px; background: linear-gradient(120deg, #f3f3f3 0%, #e4e4e4 40%, #f5f5f5 65%, #e6e6e6 100%); border-bottom: 1px solid #dcdcdc; }
  .hero-video { position: absolute; left: 106px; top: 30px; width: 472px; height: 311px; background: #111; }
  .hero-video .video-still { position: absolute; left: 4px; top: 4px; width: 464px; height: 262px; background: linear-gradient(100deg, #5b5750 0%, #8c7a6a 45%, #4b3f3a 75%, #2e2a28 100%); }
  .play-button { position: absolute; left: 206px; top: 112px; width: 60px; height: 40px; border-radius: 6px; background: rgba(0,0,0,0.75); }
  .player-bar { position: absolute; left: 4px; bottom: 4px; width: 464px; height: 37px; background: linear-gradient(#3a3a3a, #1d1d1d); }
  .player-bar .progress { position: absolute; left: 0; top: 0; width: 464px; height: 6px; background: #bdbdbd; }
  .player-bar .time { position: absolute; top: 5px; font-size: 7px; color: #ccc; }
  .hero-copy { position: absolute; left: 630px; top: 46px; }
  .hero-title { font-size: 58px; line-height: 60px; font-weight: 600; color: var(--brand-red); letter-spacing: -0.5px; }
  .hero-sub { margin-top: 10px; font-size: 25px; color: #444; }
  .hero-script { margin: 6px 0 0 70px; font-family: "Kaushan Script", cursive; font-size: 32px; color: var(--script-blue); }
  .start-button { position: absolute; left: 630px; top: 239px; width: 259px; height: 54px; border-radius: 3px; background: linear-gradient(#4a4a4a, #0b0b0b); color: #fff; font-size: 31px; font-weight: 600; text-align: center; line-height: 52px; }

  .feature { position: absolute; }
  .feature h2 { font-size: 31px; font-weight: 600; color: var(--brand-red); line-height: 36px; letter-spacing: 0.3px; }
  .feature p { margin-top: 12px; font-size: 14px; line-height: 20.4px; color: var(--text-body); }
  .feature.discussions { left: 96px; top: 604px; width: 560px; }
  .feature.discussions p { padding-left: 2px; width: 556px; }
  .feature.instruction { left: 462px; top: 860px; width: 560px; }
  .feature.instruction p { padding-left: 2px; width: 558px; }

  .feature-media { position: absolute; border: 2px solid var(--frame-border); }
  .media-discussions { left: 686px; top: 607px; width: 331px; height: 192px; background: linear-gradient(90deg, #8fc3e4 0%, #69a9d6 55%, #4e96cc 100%); }
  .media-discussions .play-ring { position: absolute; left: 122px; top: 52px; }
  .media-lesson { left: 96px; top: 866px; width: 333px; height: 194px; }
  .media-lesson .lesson-still { position: absolute; left: 0; top: 0; width: 329px; height: 160px; background: linear-gradient(90deg, #3d9ad7 0%, #52a6de 60%, #3b8fcb 100%); }
  .media-lesson .lesson-bar { position: absolute; left: 0; top: 160px; width: 329px; height: 30px; background: #f07a1e; }
  .media-lesson .lesson-bar .progress { position: absolute; left: 0; top: 0; width: 329px; height: 7px; background: #c9c9c9; }

  .site-footer { position: absolute; left: 0; top: 1100px; width: 1112px; height: 100px; background: var(--footer-bg); color: var(--footer-text); }
  .footer-links { position: absolute; left: 92px; top: 28px; font-size: 12.5px; }
  .footer-links span.sep { margin: 0 11px; }
  .copyright { position: absolute; left: 92px; top: 58px; font-size: 12.5px; }
  .footer-brand { position: absolute; left: 798px; top: 22px; font-size: 27px; line-height: 29px; font-weight: 600; color: var(--footer-mark); }
</style>
</head>
<body>
  <header class="site-header">
    <div class="brand-name">Academy of<br>Literacy Growth</div>
    <div class="search-box">
      <span>What are you curious about?</span>
      <div class="search-divider"></div>
      <svg width="18" height="20" viewBox="0 0 18 20"><circle cx="10" cy="7" r="5.5" fill="none" stroke="#2a78b8" stroke-width="2"/><line x1="6" y1="11" x2="1.5" y2="17" stroke="#2a78b8" stroke-width="2.4" stroke-linecap="round"/></svg>
    </div>
    <div class="social-links">
      <div class="social-dot navy" aria-label="Social page"></div>
      <div class="social-dot sky" aria-label="Updates channel"></div>
      <div class="social-dot orange" aria-label="News feed"></div>
      <div class="social-dot grey" aria-label="Email">
        <svg width="20" height="14" viewBox="0 0 20 14"><rect x="1" y="1" width="18" height="12" fill="none" stroke="#fff" stroke-width="1.6"/><polyline points="1,1 10,8 19,1" fill="none" stroke="#fff" stroke-width="1.6"/></svg>
      </div>
    </div>
  </header>

  <nav class="main-nav">
    <a style="left:109px">HOME</a>
    <div class="nav-sep" style="left:175px"></div>
    <a style="left:198px">FREE COURSES</a>
    <div class="nav-sep" style="left:325px"></div>
    <a style="left:349px">ACCREDITED</a>
    <div class="nav-sep" style="left:460px"></div>
    <a style="left:484px">EDUCATORS</a>
    <div class="nav-sep" style="left:591px"></div>
    <a style="left:614px">HOW IT WORKS</a>
    <div class="nav-sep" style="left:744px"></div>
    <a style="left:767px">FORUM</a>
    <div class="nav-sep" style="left:842px"></div>
    <a style="left:864px">MY STUDY CENTRE</a>
  </nav>

  <section class="hero">
    <div class="hero-video">
      <div class="video-still" role="img" aria-label="Video still of a teacher leaning on her hand, watching a live class on screen"></div>
      <div class="play-button">
        <svg width="60" height="40" viewBox="0 0 60 40"><polygon points="25,13 25,27 37,20" fill="#fff"/></svg>
      </div>
      <div class="player-bar">
        <div class="progress"></div>
        <svg style="position:absolute;left:139px;top:-1px" width="8" height="8"><circle cx="4" cy="4" r="3" fill="#eee" stroke="#555"/></svg>
        <span class="time" style="left:6px">02:16</span>
        <span class="time" style="right:6px">07:35</span>
        <svg style="position:absolute;left:6px;top:16px" width="40" height="16" viewBox="0 0 40 16"><rect x="1" y="2" width="3" height="11" fill="#ddd"/><rect x="7" y="2" width="3" height="11" fill="#ddd"/><polygon points="26,5 30,5 34,1 34,15 30,11 26,11" fill="#ddd"/></svg>
        <svg style="position:absolute;right:6px;top:15px" width="76" height="18" viewBox="0 0 76 18"><circle cx="8" cy="9" r="7" fill="#ccc"/><rect x="7" y="7" width="2" height="6" fill="#333"/><circle cx="38" cy="5" r="2.5" fill="#ccc"/><circle cx="32" cy="12" r="2.5" fill="#ccc"/><circle cx="42" cy="13" r="2.5" fill="#ccc"/><rect x="58" y="2" width="15" height="14" fill="#ccc"/></svg>
      </div>
    </div>
    <div class="hero-copy">
      <h1 class="hero-title">Live Classes</h1>
      <p class="hero-sub">for children are completely</p>
      <p class="hero-script">new in online education</p>
    </div>
    <div class="start-button">Start Now !</div>
  </section>

  <article class="feature discussions">
    <h2>During video class discussions</h2>
    <p>simply dummy text of the printing and typesetting industry. Lorem Ipsum has been the industry's standard dummy text ever since the 1500s, when an unknown printer took a galley of type and scrambled it to make a type specimen book. It has survived not only five centuries, but also the leap into electronic typesetting, remaining essentially&nbsp; It was popularised in the 1960s with the release of Letterdeck sheets containing Lorem Ipsum passages, and more recently with desktop publishing software like Pagecraft Studio including versions of Lorem Ipsumunchanged.</p>
  </article>
  <div class="feature-media media-discussions" role="img" aria-label="Video class screen with a teacher holding an open book beside a lesson whiteboard">
    <svg class="play-ring" width="80" height="80" viewBox="0 0 80 80"><circle cx="40" cy="40" r="34" fill="rgba(255,255,255,0.25)" stroke="rgba(255,255,255,0.8)" stroke-width="4"/><polygon points="32,26 32,54 55,40" fill="rgba(255,255,255,0.85)"/></svg>
  </div>

  <div class="feature-media media-lesson">
    <div class="lesson-still" role="img" aria-label="Online video lesson still of a teacher presenting a vocabulary word on a blue screen"></div>
    <div class="lesson-bar">
      <div class="progress"></div>
      <svg style="position:absolute;left:94px;top:-1px" width="9" height="9"><circle cx="4.5" cy="4.5" r="3.2" fill="#eee" stroke="#555"/></svg>
      <svg style="position:absolute;left:5px;top:10px" width="40" height="16" viewBox="0 0 40 16"><rect x="1" y="2" width="3" height="11" fill="#ffe14a"/><rect x="7" y="2" width="3" height="11" fill="#ffe14a"/><polygon points="26,5 30,5 34,1 34,15 30,11 26,11" fill="#ffe14a"/></svg>
      <svg style="position:absolute;right:6px;top:11px" width="14" height="14"><rect x="1" y="1" width="12" height="12" fill="none" stroke="#ffe14a" stroke-width="2"/></svg>
    </div>
  </div>
  <article class="feature instruction">
    <h2>Individualized online instruction</h2>
    <p>simply dummy text of the printing and typesetting industry. Lorem Ipsum has been the industry's standard dummy text ever since the 1500s, when an unknown printer took a galley of type and scrambled it to make a type specimen book. It has survived not only five centuries, but also the leap into electronic typesetting, remaining essentially&nbsp; It was popularised in the 1960s with the release of Letterdeck sheets containing Lorem Ipsum passages, and more recently with desktop publishing software like Pagecraft Studio including versions of Lorem Ipsumunchanged.</p>
  </article>

  <footer class="site-footer">
    <div class="footer-links">Home<span class="sep">|</span>Free Courses<span class="sep">|</span>Accredited<span class="sep">|</span>Educators<span class="sep">|</span>How It Works<span class="sep">|</span>Forum<span class="sep">|</span>My Study Centre</div>
    <div class="copyright">Copyright © 2014 Academy of Literacy Growth I Privacy Policy</div>
    <div class="footer-brand">Academy of<br>Literacy Growth</div>
  </footer>
</body>
</html>
```